Occupational Medical Billing and Coding Business needs Postcard

Medical billing and coding business needs marketing postcard to send to target audience of orthopaedic surgeons who practice medicine in California Workers' Compensation industry. These doctors treat injured workers and/or provide medical-legal evaluations and reports for the courts to settle the injured worker's claim. This is a highly specialized area of medical billing and coding. It is extremely complicated and can be very frustrating for doctors and their staff who do not understand the system. I would encourage the designers to check out my website: www.CorvaleHealthClaims.com
I want something bright and colorful that makes bold statements. It has to get their attention. My suggestions for bold statements include:
1) QMEs! Are your bills compliant with DWC's view? We make sure your complexity factors are maximized as well as compliant.
2) We collected over $ 462,000 just in second bill review (SBR) appeals alone and that's just one orthopaedic surgeon! Imagine what we can do for you!

I uploaded a word document with some information about the services I offer. The company logo is also there. Let me know if you need it in another format. The items with the asterisk (**) must be in the postcard.

Thank you so much!

Corvale Health Claims

Target Market(s)

Orthopaedic Surgeons who treat injured workers in California

Font styles to use
Sans Serif

Colors

Designer to choose colors to be used in the design.

Requirements
Must have
• Expert Billing and Coding Services for:
• QME - AME - IME Evaluations
• Radiology - MRI/CT Scans
• Orthopaedic Surgery
• Certified Coders on Staff
• Electronic Claim Submission
• Payment within 15 days
• It's important to spell orthopaedic with the "A" after the "P" as it is an acknowledgment of the origins of the practice and will attract a doctor with higher education.

```html
<!DOCTYPE html>
<html lang="en">
<head>
<meta charset="utf-8">
<title>Corvale Health Claims – Postcard</title>
<link href="https://fonts.googleapis.com/css2?family=Lato:ital,wght@0,400;0,700;1,400;1,700&family=Marcellus+SC&display=swap" rel="stylesheet">
<style>
  :root{
    --navy:#33407d;
    --green:#8db33a;
    --ink:#1d1d1d;
    --white:#ffffff;
    --page:#e8e8e8;
    --photo-a:#dfe8f0;
    --photo-b:#b9c9d9;
    --rule:#8a8a8a;
  }
  *{box-sizing:border-box;margin:0;padding:0}
  html,body{width:902px;height:1200px;overflow:hidden;background:var(--page)}
  body{font-family:"Lato",Arial,sans-serif;color:var(--ink);position:relative}
  .card{position:absolute;left:41px;width:820px;background:var(--white);overflow:hidden;box-shadow:0 4px 14px rgba(0,0,0,.25)}
  .card--front{top:20px;height:560px}
  .card--back{top:620px;height:560px}
  .shapes{position:absolute;inset:0}
  .abs{position:absolute}
  .wordmark{font-family:"Lato",Arial,sans-serif;font-weight:400;color:var(--ink);letter-spacing:.5px;line-height:1.1}
  .serif-caps{font-family:"Marcellus SC",Georgia,serif}

  /* front */
  .photo{position:absolute;left:0;top:150px;width:400px;height:372px;background:linear-gradient(160deg,var(--photo-a),var(--photo-b))}
  .front-logo{left:40px;top:58px;font-size:30px;width:300px}
  .hook{right:28px;top:20px;width:400px;text-align:center}
  .hook h2{color:var(--white);font-size:23px;font-weight:400;line-height:1.15;letter-spacing:.5px}
  .hook p{color:var(--navy);font-size:15px;text-transform:uppercase;margin-top:8px;line-height:1.2;letter-spacing:.3px}
  .claim{right:28px;top:204px;width:430px;text-align:right;font-weight:700;font-size:16px;line-height:1.3}
  .services{left:378px;top:294px;width:430px;color:var(--white)}
  .services h3{font-size:17px;font-weight:400;letter-spacing:.5px;text-align:center;margin-bottom:8px}
  .cols{display:flex;gap:10px}
  .cols ul{list-style:none;font-style:italic;font-size:12px;line-height:1.35}
  .cols ul:first-child{width:222px}
  .cols ul:last-child{width:198px}
  .cols li{position:relative;padding-left:22px}
  .cols li::before{content:"";position:absolute;left:2px;top:4px;width:8px;height:8px;border-radius:50%;background:var(--white)}
  .contact-label{right:28px;top:450px;font-weight:700;font-size:16px}
  .front-contact{right:28px;top:474px;text-align:right;color:var(--white)}
  .front-contact .phone{font-size:25px;font-weight:700;display:flex;align-items:center;justify-content:flex-end;gap:8px;line-height:1.05}
  .front-contact .mail{font-size:14px;display:flex;align-items:center;justify-content:flex-end;gap:8px;margin-top:2px}
  .web-band{left:0;top:522px;width:820px;height:38px;color:var(--white);font-weight:700;font-size:18px;display:flex;align-items:center;justify-content:center}

  /* back */
  .flap{position:absolute;left:0;top:0;width:410px;height:560px;box-shadow:6px 0 10px rgba(0,0,0,.18)}
  .collect{left:22px;top:22px;width:366px;color:var(--white)}
  .collect h2{font-size:20px;font-weight:400;text-align:center;line-height:1.1;margin-bottom:10px}
  .collect p{font-size:12px;line-height:1.35;margin-bottom:8px}
  .about{left:22px;top:256px;width:366px}
  .about h2{font-size:19px;font-weight:400;text-align:center;margin-bottom:6px}
  .about p{font-size:10.5px;line-height:1.35;text-align:justify}
  .back-contact{left:28px;top:462px;color:var(--ink);font-weight:700;font-size:13px;line-height:1.5}
  .back-contact div{display:flex;align-items:center;gap:8px}
  .back-logo{left:445px;top:44px;font-size:20px;width:200px}
  .stamp{left:680px;top:34px;width:100px;height:110px;border:2px solid #b5b5b5}
  .address-line{left:470px;width:300px;height:0;border-top:1.5px solid var(--rule)}
</style>
</head>
<body>

<section class="card card--front">
  <div class="photo" role="img" aria-label="Photo of a smiling female doctor giving a thumbs up with a male doctor behind her"></div>
  <svg class="shapes" viewBox="0 0 820 560" width="820" height="560" aria-hidden="true">
    <path d="M470 0 H820 V195 H380 C400 115 430 50 470 0 Z" fill="var(--green)"/>
    <path d="M350 284 H820 V444 H362 C342 395 340 335 350 284 Z" fill="var(--navy)"/>
    <path d="M380 472 H820 V522 H336 C352 505 366 490 380 472 Z" fill="var(--green)"/>
    <rect x="0" y="522" width="820" height="38" fill="var(--navy)"/>
  </svg>

  <div class="abs wordmark front-logo">Corvale Health Claims</div>

  <div class="abs hook">
    <h2 class="serif-caps">QMEs! Are your bills<br>compliant with DWC's view?</h2>
    <p>We make sure your complexity factors<br>are maximized as well as compliant.</p>
  </div>

  <p class="abs claim">We collected over $ 462,000 just in second bill review (SBR) appeals alone and that's just one orthopaedic surgeon! Imagine what we can do for you!</p>

  <div class="abs services">
    <h3 class="serif-caps">Expert Billing and Coding Services for:</h3>
    <div class="cols">
      <ul>
        <li>QME – AME – IME Evaluations</li>
        <li>Radiology – MRI/CT Scans</li>
        <li>Electrodiagnostic Studies</li>
        <li>Orthopaedic Surgery</li>
        <li>Ambulatory Surgery Centers</li>
        <li>Treatment – Primary/Secondary Physician</li>
      </ul>
      <ul>
        <li>Certified Coders on Staff</li>
        <li>Electronic Claim Submission</li>
        <li>Payment within 15 days</li>
        <li>Over 25 Years Experience in Workers' Comp</li>
      </ul>
    </div>
  </div>

  <div class="abs contact-label">CONTACT US TODAY:</div>
  <div class="abs front-contact">
    <div class="phone">
      <svg width="22" height="22" viewBox="0 0 24 24" aria-hidden="true"><circle cx="12" cy="12" r="10.5" fill="none" stroke="var(--navy)" stroke-width="2"/><path d="M8.5 6.5l2 2-1.2 1.5c.8 1.7 2 2.9 3.7 3.7l1.5-1.2 2 2-1.3 1.8c-4 -.3-7.9-4.2-8.2-8.2z" fill="var(--navy)"/></svg>
      714. 555.0182
    </div>
    <div class="mail">
      <svg width="16" height="12" viewBox="0 0 16 12" aria-hidden="true"><rect x="0.5" y="0.5" width="15" height="11" fill="var(--navy)"/><path d="M1 1l7 5.5L15 1" fill="none" stroke="var(--white)" stroke-width="1.2"/></svg>
      info@CorvaleHealthClaims.com
    </div>
  </div>
  <div class="abs web-band">Visit our Website for more information : www.CorvaleHealthClaims.com</div>
</section>

<section class="card card--back">
  <div class="flap">
    <svg class="shapes" viewBox="0 0 410 560" width="410" height="560" aria-hidden="true">
      <path d="M0 0 H410 V226 C280 206 130 212 0 242 Z" fill="var(--navy)"/>
      <path d="M0 242 C130 212 280 206 410 226" fill="none" stroke="var(--green)" stroke-width="4"/>
      <rect x="12" y="454" width="398" height="72" fill="var(--green)"/>
    </svg>

    <div class="abs collect">
      <h2 class="serif-caps">We also provide<br>collection services:</h2>
      <p>Expert Denial Management: Timely filing of SBR and IBR Appeals- Collected over $462,000 just in second bill review appeals. This is an example of ONE orthopaedic surgeon to date. Imagine what we can do for you!</p>
      <p>Don't let insurance companies "zero-out" your QME and AME bills. We get your medical-legal bills paid including penalty, interest and costs associated with the effort to collect.</p>
    </div>

    <div class="abs about">
      <h2 class="serif-caps">About us</h2>
      <p>We are a results driven medical billing service specializing in California workers' compensation. Our long history in this ever-changing industry has taught us we need to keep our finger on the pulse. We use the latest, greatest software and stay up-to-date on the changing rules, regulations, and trends. We're proud to offer specialized Medical Billing and Collection Services for all types of industrial medical providers and facilities. Our billing services are tailored to your individual practice. We can increase your accounts receivables, reduce your write offs and keep you compliant with the regulations at the same time. Contact us today to get in touch with our team of experienced professionals.</p>
    </div>

    <div class="abs back-contact">
      <div><svg width="13" height="13" viewBox="0 0 24 24" aria-hidden="true"><circle cx="12" cy="12" r="10.5" fill="none" stroke="var(--ink)" stroke-width="2"/><path d="M8.5 6.5l2 2-1.2 1.5c.8 1.7 2 2.9 3.7 3.7l1.5-1.2 2 2-1.3 1.8c-4-.3-7.9-4.2-8.2-8.2z" fill="var(--ink)"/></svg>714. 555.0182</div>
      <div><svg width="13" height="10" viewBox="0 0 16 12" aria-hidden="true"><rect x="0.5" y="0.5" width="15" height="11" fill="none" stroke="var(--ink)"/><path d="M1 1l7 5.5L15 1" fill="none" stroke="var(--ink)" stroke-width="1.2"/></svg>info@CorvaleHealthClaims.com</div>
      <div><svg width="13" height="13" viewBox="0 0 24 24" aria-hidden="true"><circle cx="12" cy="12" r="10" fill="none" stroke="var(--ink)" stroke-width="2"/><ellipse cx="12" cy="12" rx="4.5" ry="10" fill="none" stroke="var(--ink)" stroke-width="1.6"/><path d="M2 12h20" stroke="var(--ink)" stroke-width="1.6"/></svg>www.corvalehealthclaims.com</div>
    </div>
  </div>

  <div class="abs wordmark back-logo">Corvale Health Claims</div>
  <div class="abs stamp"></div>
  <div class="abs address-line" style="top:300px"></div>
  <div class="abs address-line" style="top:370px"></div>
  <div class="abs address-line" style="top:440px"></div>
</section>

</body>
</html>
```